依頼詳細
商品コンセプトは、「しぼりたて」・「冬」・「雪」・「自然」
「遊び心」・「明るい」・「楽しい」・「インパクトのあるデザイン」
女性や若い方にも、手に取って頂けるような、明るくポップな
デザインを募集いたします。

日本酒というイメージに拘らない、新しい感覚のデザインを希望いたします。
記載項目
ボトルサイズ 720mlのラベルサイズ
H 77mm × W 128mm

ボトルサイズ 1800mlのラベルサイズ
H 138mm × W 160mm

ラベル材質 : 紙・和紙・コート紙・光沢紙等は可能です。
クリアなフィルムや透明な素材は不可です。

ブランドロゴマーク配置必須
希望イメージ
シンプル 複雑
単色 カラフル
暗い 明るい
日常 高級
遊び心 厳粛
未来的 伝統的
女性的 男性的
希望する色
緑系、青系、水色系
納品ファイル
• 高解像度JPG (.jpg)
• イラストレーター形式 (.ai)
• フォトショップ形式 (.psd)
補足説明
■ 選んだ理由

ご提案ありがとうございました。
こちらのデザインを採用させていただきました点といたしましては、
冬の雪つむぎ岳の美しさと、透き通った冷たさが、良く表現されており、
雪の結晶の繊細な部分が、美しく、冬限定のお酒というのが
わかりやすかった所も、ポイントです。

■ 提案者全員のお礼・コメント

この度は、沢山のご提案誠にありがとうございました。
皆様洗練されたデザインで、定番のイメージのものから、斬新なイメージのものまで
幅広い、提案をいただき、素晴らしいデザインが多数あり、社内でも意見が分かれました。
この度は、誠にありがとうございました。

```html
<!DOCTYPE html>
<html lang="ja">
<head>
<meta charset="utf-8">
<title>雪つむぎ しぼりたて ラベル</title>
<link href="https://fonts.googleapis.com/css2?family=Klee+One:wght@600&family=Zen+Kaku+Gothic+New:wght@400&display=swap" rel="stylesheet">
<style>
  :root {
    --canvas-bg: #f4f5f6;
    --label-blue: #a9cbe9;
    --label-blue-light: #c4dcf1;
    --snow-white: #ffffff;
    --ink-white: #ffffff;
    --ink-grey: #8a9aa8;
  }
  html, body {
    margin: 0;
    padding: 0;
    width: 800px;
    height: 1200px;
    overflow: hidden;
    background: var(--canvas-bg);
  }
  .canvas {
    position: relative;
    width: 800px;
    height: 1200px;
    display: flex;
    align-items: center;
    justify-content: center;
  }
  .label {
    position: relative;
    width: 720px;
    height: 433px;
    background: var(--label-blue);
    box-shadow: 0 2px 10px rgba(60, 90, 120, 0.12);
    overflow: hidden;
  }
  .snow-field {
    position: absolute;
    left: 0;
    top: 0;
    width: 720px;
    height: 360px;
    background:
      radial-gradient(ellipse at 20% 25%, rgba(255,255,255,0.55) 0%, rgba(255,255,255,0) 45%),
      radial-gradient(ellipse at 78% 40%, rgba(255,255,255,0.5) 0%, rgba(255,255,255,0) 50%),
      radial-gradient(ellipse at 50% 85%, rgba(255,255,255,0.45) 0%, rgba(255,255,255,0) 55%),
      linear-gradient(180deg, var(--label-blue) 0%, var(--label-blue-light) 100%);
  }
  .brand-name {
    position: absolute;
    left: 52px;
    top: 34px;
    writing-mode: vertical-rl;
    font-family: "Klee One", cursive;
    font-weight: 600;
    font-size: 30px;
    letter-spacing: 4px;
    color: var(--ink-white);
    margin: 0;
  }
  .product-name {
    position: absolute;
    left: 150px;
    top: 200px;
    font-family: "Klee One", cursive;
    font-weight: 600;
    font-size: 52px;
    letter-spacing: 10px;
    color: var(--ink-white);
    margin: 0;
  }
  .footer-band {
    position: absolute;
    left: 0;
    bottom: 0;
    width: 720px;
    height: 80px;
    background: var(--snow-white);
  }
  .footer-band svg {
    position: absolute;
    left: 0;
    top: -14px;
  }
  .brewery {
    position: absolute;
    left: 0;
    right: 0;
    bottom: 28px;
    text-align: center;
    font-family: "Zen Kaku Gothic New", sans-serif;
    font-size: 14px;
    letter-spacing: 3px;
    color: var(--ink-grey);
    margin: 0;
  }
</style>
</head>
<body>
  <div class="canvas">
    <section class="label">
      <div class="snow-field" role="img" aria-label="Pattern of falling snow: white snowflake dots of many sizes scattered over pale blue"></div>
      <h1 class="brand-name">雪つむぎ</h1>
      <p class="product-name">しぼりたて</p>
      <div class="footer-band">
        <svg width="720" height="16" viewBox="0 0 720 16" aria-hidden="true">
          <path d="M0 16 Q180 2 360 10 T720 6 L720 16 Z" fill="var(--snow-white)"/>
        </svg>
        <p class="brewery">YUKITSUMUGI SAKE</p>
      </div>
    </section>
  </div>
</body>
</html>
```